Label Design for Nuts package*

Develop the design for a label for nuts sold in a paperbag.

you can find our website here: www.kornfeld-snack.de.
Here comes the link to our catalogue: https://www.blattwerk-docs.com/de/document/read/48172956/kornfeld-premium-snacks-gesamtkatalog-2019

With this product we are targeting private customers who want to buy nuts with plastic free packaging online.
The colours of the label should fit the brown paper bag.

```html
<!DOCTYPE html>
<html lang="de">
<head>
<meta charset="utf-8">
<title>Kornfeld Premium Snacks – Cashew Kerne</title>
<link rel="stylesheet" href="https://fonts.googleapis.com/css2?family=Josefin+Sans:wght@300;400&family=Crimson+Text:wght@600&display=swap">
<style>
  :root {
    --backdrop: #e2b0b2;
    --brown: #7b3c37;
    --brown-deep: #6b302c;
    --kraft: #d5b08a;
    --kraft-light: #dcb993;
    --white: #fbf4ee;
  }
  * { margin: 0; padding: 0; box-sizing: border-box; }
  html, body { width: 1200px; height: 1000px; overflow: hidden; }
  body {
    background: var(--backdrop);
    position: relative;
    font-family: "Josefin Sans", sans-serif;
    color: var(--brown-deep);
  }

  /* Header brand */
  .brand-header {
    position: absolute;
    left: 0; top: 58px; width: 1200px;
    text-align: center;
  }
  .brand-mark {
    display: block;
    width: 44px; height: 44px;
    margin: 0 auto 14px;
    border-radius: 50%;
    background: var(--brown-deep);
  }
  .brand-name {
    font-weight: 300;
    font-size: 54px;
    letter-spacing: 4px;
    line-height: 1;
    color: var(--brown-deep);
  }
  .brand-tagline {
    margin-top: 12px;
    font-family: "Crimson Text", serif;
    font-weight: 600;
    font-size: 17px;
    letter-spacing: 3px;
    color: var(--brown-deep);
  }
  .brand-rule {
    width: 220px; height: 1px;
    margin: 10px auto 0;
    background: var(--brown-deep);
  }

  /* Flat bag front */
  .bag {
    position: absolute;
    left: 378px; top: 345px;
    width: 434px; height: 597px;
    background: var(--kraft);
    overflow: hidden;
  }
  .bag-pattern {
    position: absolute;
    left: 0; top: 0; width: 100%; height: 272px;
    background: linear-gradient(180deg, var(--brown) 0%, #82443d 100%);
  }
  .label-arch {
    position: absolute;
    left: 92px; top: 218px;
    width: 250px; height: 250px;
    border-radius: 50%;
    background: var(--kraft-light);
  }
  .label-body {
    position: absolute;
    left: 0; top: 270px; width: 100%; height: 282px;
    background: var(--kraft);
  }
  .label-brand {
    position: absolute;
    left: 0; top: 236px; width: 100%;
    text-align: center;
  }
  .label-brand .brand-mark {
    width: 26px; height: 26px; margin-bottom: 12px;
  }
  .label-brand .brand-name { font-size: 38px; letter-spacing: 3px; }
  .label-brand .brand-tagline { font-size: 12.5px; margin-top: 7px; letter-spacing: 2px; }
  .label-brand .brand-rule { width: 150px; margin-top: 6px; }

  .product-name {
    position: absolute;
    font-weight: 400;
    font-size: 62px;
    letter-spacing: 6px;
    line-height: 1;
    color: var(--brown);
  }
  .product-name.line-1 { left: 8px; top: 380px; }
  .product-name.line-2 { right: 6px; top: 442px; }

  .bag-footer {
    position: absolute;
    left: 0; bottom: 0; width: 100%; height: 45px;
    background: var(--brown);
    display: flex; align-items: center; justify-content: center;
  }
  .bag-url {
    font-size: 12px;
    letter-spacing: 0.5px;
    color: var(--white);
  }
</style>
</head>
<body>
  <header class="brand-header">
    <span class="brand-mark"></span>
    <div class="brand-name">KORNFELD</div>
    <div class="brand-tagline">PREMIUM SNACKS</div>
    <div class="brand-rule"></div>
  </header>

  <main class="bag">
    <div class="bag-pattern" role="img" aria-label="Hand-drawn pattern of scattered cashew nuts on brown"></div>
    <div class="label-arch"></div>
    <div class="label-body"></div>

    <div class="label-brand">
      <span class="brand-mark"></span>
      <div class="brand-name">KORNFELD</div>
      <div class="brand-tagline">PREMIUM SNACKS</div>
      <div class="brand-rule"></div>
    </div>

    <h1 class="product-name line-1">CASHEW</h1>
    <div class="product-name line-2">KERNE</div>

    <footer class="bag-footer">
      <span class="bag-url">www.kornfeld-snack.de</span>
    </footer>
  </main>
</body>
</html>
```